- Redesign our business card
- Logo remains unchanged
- Current business card attached

Target Market(s)

We are a property management company

Industry/Entity Type

Business

```html
<!DOCTYPE html>
<html lang="en">
<head>
<meta charset="utf-8">
<title>Harlow Property Group – Business Card</title>
<link href="https://fonts.googleapis.com/css2?family=Source+Sans+3:wght@400;600&display=swap" rel="stylesheet">
<style>
  :root {
    --page-bg: #b4b4b4;
    --card-white: #ffffff;
    --olive: #827e44;
    --sand: #dfd2a8;
    --slate: #6a6a70;
    --ink: #4a4a4a;
    --title-grey: #7a7a72;
  }
  * { box-sizing: border-box; margin: 0; padding: 0; }
  html, body {
    width: 1200px;
    height: 900px;
    overflow: hidden;
    background: var(--page-bg);
    font-family: "Source Sans 3", "Helvetica Neue", Arial, sans-serif;
  }
  .canvas {
    position: relative;
    width: 1200px;
    height: 900px;
  }
  .card {
    position: absolute;
    left: 340px;
    width: 520px;
    height: 300px;
    border-radius: 22px;
    overflow: hidden;
    background: var(--card-white);
  }
  .card--front { top: 130px; }
  .card--back  { top: 460px; }

  /* Front */
  .brand {
    position: absolute;
    left: 150px;
    top: 170px;
  }
  .brand__name {
    display: flex;
    align-items: center;
    gap: 10px;
    font-size: 17px;
    font-weight: 400;
    letter-spacing: 0.08em;
    text-transform: uppercase;
    color: var(--olive);
  }
  .brand__square {
    width: 12px;
    height: 12px;
    background: var(--olive);
  }
  .brand__tagline {
    margin-top: 4px;
    margin-left: 22px;
    font-size: 11px;
    letter-spacing: 0.1em;
    text-transform: uppercase;
    color: var(--slate);
  }

  /* Back */
  .card__bands {
    position: absolute;
    inset: 0;
    width: 100%;
    height: 100%;
  }
  .band--olive { fill: var(--olive); }
  .band--sand  { fill: var(--sand); }
  .band--slate { fill: var(--slate); }

  .contact {
    position: absolute;
    left: 44px;
    top: 80px;
  }
  .contact__name {
    font-size: 19px;
    font-weight: 400;
    letter-spacing: 0.06em;
    text-transform: uppercase;
    color: var(--olive);
    line-height: 1.1;
  }
  .contact__role {
    font-size: 13px;
    color: var(--title-grey);
    margin-top: 2px;
  }
  .contact__details {
    list-style: none;
    margin-top: 18px;
    font-size: 10.5px;
    line-height: 13.5px;
    color: var(--ink);
    text-transform: uppercase;
  }
  .contact__details .lower { text-transform: none; }
  .contact__label { display: inline-block; width: 14px; }
</style>
</head>
<body>
<main class="canvas">

  <section class="card card--front" aria-label="Business card front">
    <div class="brand">
      <div class="brand__name"><span class="brand__square"></span>Harlow Property Group</div>
      <div class="brand__tagline">Strata Management Services</div>
    </div>
  </section>

  <section class="card card--back" aria-label="Business card back">
    <svg class="card__bands" viewBox="0 0 520 300" preserveAspectRatio="none" aria-hidden="true">
      <rect class="band--olive" x="116" y="0" width="372" height="300"/>
      <polygon class="band--sand" points="0,64 310,24 282,300 0,300"/>
      <rect class="band--slate" x="486" y="0" width="34" height="300"/>
    </svg>
    <div class="contact">
      <h1 class="contact__name">Daniel Harlow</h1>
      <p class="contact__role">Licensed Strata Manager</p>
      <ul class="contact__details">
        <li>PO Box 48, Ridgeway Hills NSW 2031</li>
        <li>12/6-18 Marlow Street Eastbrook NSW 2044</li>
        <li><span class="contact__label">T:</span>02 9450 1187</li>
        <li><span class="contact__label">F:</span>02 9450 1192</li>
        <li><span class="contact__label">M:</span>0418 362 709</li>
        <li class="lower"><span class="contact__label">E:</span>info@harlowproperty.com.au</li>
        <li class="lower">www.harlowproperty.com.au</li>
      </ul>
    </div>
  </section>

</main>
</body>
</html>
```